cover for CD- Single.

This design is for a CD cover. The design is at your disposal, using all of your creative talents.
Things to improve the photo: Cleaning the face, removing blemishes.
Design in black and white would be an option (Color would be another option). I reiterate it is up to your taste and criteria, any reform and art on the cover of Cd.
Name of the single: El Camino del Alba Serena
Artist Name: Marisol Quenteva

Target Market(s)

Single Music

Industry/Entity Type

Music

Colors

Designer to choose colors to be used in the design.

Requirements
Must have
• style, elegance, professionalism, spontaneity
Nice to have
• I want it to be as professional as possible.
Should not have
• Spelling errors.

```html
<!DOCTYPE html>
<html lang="es">
<head>
<meta charset="utf-8">
<title>El Camino del Alba Serena — Marisol Quenteva</title>
<link rel="stylesheet" href="https://fonts.googleapis.com/css2?family=Questrial&display=swap">
<style>
  :root {
    --frame-salmon: #eeaaa0;
    --photo-light: #f4c4b8;
    --photo-mid: #ef8f8e;
    --photo-deep: #e23a58;
    --photo-shadow: #9a2646;
    --type-white: rgba(255, 240, 236, 0.62);
  }
  html, body {
    margin: 0;
    padding: 0;
    overflow: hidden;
    background: var(--frame-salmon);
  }
  .cover {
    position: relative;
    width: 1200px;
    height: 1200px;
    background: var(--frame-salmon);
    overflow: hidden;
  }
  .cover-art {
    position: absolute;
    inset: 0;
    width: 1200px;
    height: 1200px;
    display: block;
  }
  .cover-title,
  .cover-artist {
    font-family: "Questrial", "Century Gothic", sans-serif;
    fill: var(--type-white);
    text-anchor: middle;
    font-size: 170px;
    letter-spacing: 2px;
  }
</style>
</head>
<body>
  <main class="cover">
    <svg class="cover-art" viewBox="0 0 1200 1200" xmlns="http://www.w3.org/2000/svg">
      <defs>
        <linearGradient id="portrait-tone" x1="0" y1="0.2" x2="1" y2="0.8">
          <stop offset="0" stop-color="var(--photo-light)"/>
          <stop offset="0.45" stop-color="var(--photo-mid)"/>
          <stop offset="0.8" stop-color="var(--photo-deep)"/>
          <stop offset="1" stop-color="var(--photo-shadow)"/>
        </linearGradient>
      </defs>

      <rect class="portrait" x="50" y="50" width="1098" height="1098"
            fill="url(#portrait-tone)" role="img"
            aria-label="Portrait photograph of the singer with eyes closed, tinted in pink and red"/>

      <g class="cover-title" aria-label="El Camino del Alba Serena">
        <text x="600" y="272">EL CAMINO</text>
        <text x="600" y="457">DEL ALBA</text>
        <text x="600" y="642">SERENA</text>
      </g>
      <g class="cover-artist" aria-label="Marisol Quenteva">
        <text x="600" y="845">MARISOL</text>
        <text x="600" y="1035">QUENTEVA</text>
      </g>
    </svg>
  </main>
</body>
</html>
```